I am looking for a web design that includes space for a blog, archive and an
“ about me” section. It should be capable of being updated in the future should I decide to build the site. I like edgy, creative, friendly and inviting to go with my logo style.
The Plate Ledger is an approach to breaking down and rebuilding or just tweaking what needs to be done to reach nutritional fitness. That is the actual workout part....journaling through something I call reflective nutrition. By doing this one can actually see what they are doing well and where they may need to improve. It involves goal setting and analyzing one's relationship with food. the workout is more mental in this approach. Physical activity is definitely a part of a strong nutritional foundation, but here I am focusing on the work that goes into creating a positive nutritionally fit person.

1. Blog Section: this will be the foundation of the website. I will write weekly blogs explaining and encouraging readers to use reflective nutrition approach to discover and explore their relationship with food and create healthy nutritional habits, breaking those that have been detrimental thus far. Journaling and realistic goal setting is the key to this approach.

2. Archive: this is the section to store old blogs by date with ability to retrieve and read again. Readers should gave access to this section.

3. About Me: I am a clinical nutritionist with a Bachelors of Science and Masters of Science in Nutrition. I have over 30 years experience working with both inpatient and outpatient populations covering a myriad of conditions requiring nutritional intervention. I am passionate about my field and my goal is to help others achieve their optimal nutritional health. I will share my personal struggle with attaining nutritional fitness. I have the
unique perspective of being both a nutrition professional and patient.
Please note that my blog name is not the name under which I am registered with the Board For Dietary Credentialing (BDC).Contact me privately if you require more information.
Thank you for stopping by and I hope you will come back.
Peace,
M. Harlow
4. Contact Me: This section will only contain my email address for comments and suggestions Theplateledger@mailnest.example
Updates

Hey guys! I am very new to this process and I apologize for not having much detail. I think I added more that may give you a clearer understanding of my project. I know I said that I didn't plan on using illustrations but I am getting a better picture of what you do. Please use all your creative tools and talents and imaginations! But read my description of what the actual nutrition workout is. It is more of a mental not physical workout. I will respond to your questions and suggestions. I welcome them. Have fun with this!!! I look forward to seeing your work. . Peace, Mira

Target Market(s)

Anyone interested in a realistic approach to reaching nutrition goals.

Industry/Entity Type

Nutrition

Coding

Coded - Design and coding required

Number of Pages Required

3 page

Colors
fbee3d
ffc214

Requirements
Must have
• An automatic sign-off signature at the end of each blog, preferably in the same font as my logo name. Signature will read:
Peace,
B.
My blog name is M, Harlow
Complementary color scheme to the logo but not white, if at all possible. I don't plan on using illustrations so I am relying on the web design to draw people in. It cannot be dull or bland but still professional.
It must be inviting and personable, not intimidating
I may want to update and add on later. Site should be capable of doing
that....should be buildable.
I love the font that was used in the name of my logo and would like to stay consistant with that, if possible.
Nice to have
• A way to monitor people who visit and return.
Maybe a counter to see how many people have visited
Would it be possible to prominently display my logo on the first page with my contact information and have that open directly to my blog page? Also, would the block page have to be a white background? I prefer it to be a color if that is complementary to the logo olor scheme
Should not have
• Please no illustrations of a gym.
This isn’t a blog about physical fitness. It is a blog requiring people to think about what they consume on a daily basis, breaking bad eating habits and creating positive, healthy ones.
I tried to get pictures and illustrations to use but due to licensure restrictions, I was unable at this time. Although your designs are brilliant, I may not be able to supply appropriate illustrations to do your designs justice.

```html
<!DOCTYPE html>
<html lang="en">
<head>
<meta charset="utf-8">
<title>The Plate Ledger</title>
<link rel="stylesheet" href="https://fonts.googleapis.com/css2?family=Poppins:wght@400;500;600;700&family=PT+Serif&family=Caveat+Brush&family=Allura&display=swap">
<style>
:root{
  --gold:#c4a610;
  --gold-dark:#b39709;
  --ink:#1f1f1f;
  --text:#333333;
  --muted:#8a8a8a;
  --white:#ffffff;
  --line:#d9d9d9;
}
*{box-sizing:border-box;margin:0;padding:0}
html,body{width:1200px;height:3029px;overflow:hidden}
body{position:relative;background:var(--white);font-family:'Poppins',sans-serif;color:var(--ink)}
.abs{position:absolute}

/* header */
.site-header{left:0;top:0;width:1200px;height:83px;background:var(--white)}
.brand-tab{left:73px;top:0;width:130px;height:180px;background:var(--white);clip-path:polygon(0 0,100% 0,100% 88%,0 100%);z-index:3;display:flex;flex-direction:column;align-items:center;justify-content:center;gap:10px;padding-bottom:20px}
.brand-dot{width:46px;height:46px;border-radius:50%;background:var(--gold)}
.brand-name{font-weight:600;font-size:17px;line-height:1.15;text-align:center;color:var(--gold)}
.main-nav{top:46px;left:586px;display:flex}
.main-nav a{font-size:15px;color:var(--text);text-decoration:none;margin-right:43px}
.nav-dot{left:600px;top:14px;width:22px;height:22px;border-radius:50%;background:var(--gold)}

/* hero */
.hero{left:0;top:83px;width:1200px;height:374px}
.hero-photo{position:absolute;inset:0;background:linear-gradient(90deg,#e3e5e7 0%,#c9d3d4 18%,#4f8e96 38%,#c49a2a 55%,#d9b140 64%,#e7e4de 78%,#b8b6ae 88%,#3f5f2c 100%)}
.hero-circle{left:210px;top:95px;width:200px;height:200px;border-radius:50%;background:var(--gold);opacity:.9}
.hero-title{left:430px;top:127px;font-family:'Caveat Brush',cursive;font-size:84px;color:var(--ink);text-shadow:3px 3px 0 var(--white),-2px -2px 0 var(--white),2px -2px 0 var(--white),-2px 2px 0 var(--white);white-space:nowrap}
.btn{display:flex;align-items:center;justify-content:center;background:var(--gold);color:var(--white);font-weight:600;font-size:16px;border-top-left-radius:28px;text-transform:uppercase;text-decoration:none}
.hero .btn{position:absolute;left:458px;top:237px;width:168px;height:47px}

/* intro columns */
.intro-col{top:508px;width:290px}
.intro-col h3{font-weight:600;font-size:23px;margin-bottom:16px}
.intro-col p{font-family:'PT Serif',serif;font-size:14px;line-height:22px;color:var(--text)}
.btn-facts{left:478px;top:706px;width:242px;height:47px}

/* about */
.about-script{left:0;width:1200px;top:845px;text-align:center;font-family:'Allura',cursive;font-size:118px;color:#cfcfcf;white-space:nowrap}
.about-title{left:0;width:1200px;top:900px;text-align:center;font-weight:600;font-size:42px;color:var(--gold)}
.about-text{left:190px;width:820px;top:983px;text-align:center;font-family:'PT Serif',serif;font-size:14px;line-height:22px;color:var(--text)}

/* blog */
.blog-band{left:0;top:1106px;width:1200px;height:569px;background:var(--gold)}
.blog-title{left:0;width:1200px;top:1158px;text-align:center;font-weight:700;font-size:56px;color:var(--white)}
.post-card{top:1260px;width:328px;height:336px;background:var(--white);box-shadow:0 2px 6px rgba(0,0,0,.15);padding:30px 12px 0 20px}
.post-tags{font-size:11.5px;color:var(--ink);display:flex;gap:18px}
.post-cat{font-size:11.5px;font-weight:600;color:var(--gold);margin-top:8px}
.post-card h4{font-weight:600;font-size:21.5px;line-height:25px;letter-spacing:-0.2px;margin:10px 0 0 3px}
.post-card p{font-family:'PT Serif',serif;font-size:13.5px;line-height:22px;color:var(--text);margin:12px 0 0 3px;padding-right:8px}
.post-meta{position:absolute;left:14px;right:14px;top:275px;border-top:1px solid var(--line);padding-top:16px;display:flex;align-items:center;justify-content:space-between;font-size:13px;color:var(--muted)}
.post-meta .date{display:flex;align-items:center;gap:8px;padding-left:5px}

.btn-more{left:478px;top:1723px;width:242px;height:47px}

/* archive */
.archive-title{left:0;width:1200px;top:1816px;text-align:center;font-weight:600;font-size:54px;color:var(--ink)}
.archive-card{background:var(--gold);padding:28px 24px}
.archive-card h4{font-weight:600;font-size:22px;line-height:26px;color:var(--ink)}
.archive-card p{font-family:'PT Serif',serif;font-size:13.5px;line-height:22px;color:var(--ink);margin-top:20px}
.archive-date{display:flex;align-items:center;gap:10px;font-size:13.5px;color:var(--white);margin-top:24px}

/* partners */
.partner-band{left:0;top:2450px;width:1200px;height:150px;background:var(--gold);display:flex;align-items:center;justify-content:space-around;padding:0 110px}
.partner{font-weight:700;font-size:20px;color:var(--white)}

/* footer */
.foot-h{font-weight:600;font-size:26px;color:var(--ink)}
.contact-row{left:92px;display:flex;gap:22px;font-size:15px;line-height:22px;color:var(--ink)}
.contact-row svg{flex:none;margin-top:2px}
.menu-row{left:512px;display:flex;gap:25px;font-size:15px;color:var(--ink);align-items:center}
.foot-brand{left:830px;top:2665px;width:175px;display:flex;flex-direction:column;align-items:center;gap:14px}
.foot-brand .brand-dot{width:80px;height:80px}
.foot-brand .brand-name{font-size:26px}
.social{top:2862px;width:22px;height:22px;border-radius:50%;background:var(--gold)}
.copyright{left:0;width:1200px;top:2988px;text-align:center;font-size:13px;color:var(--ink)}
</style>
</head>
<body>

<header class="abs site-header">
  <div class="abs nav-dot"></div>
  <nav class="abs main-nav">
    <a href="#">Home</a><a href="#">About Me</a><a href="#">Services</a><a href="#">Blog</a><a href="#">Contact Us</a>
  </nav>
</header>
<div class="abs brand-tab">
  <span class="brand-dot"></span>
  <span class="brand-name">The Plate<br>Ledger</span>
</div>

<section class="abs hero">
  <div class="hero-photo" role="img" aria-label="Woman in a yellow sweater writing in a journal on a teal chair beside sunflowers and a plant"></div>
  <div class="abs hero-circle"></div>
  <h1 class="abs hero-title">The Plate Ledger</h1>
  <a class="btn">Read More</a>
</section>

<section>
  <div class="abs intro-col" style="left:133px"><h3>Lorem ipsum</h3><p>Quis autem vel eum iure reprehenderit qui in ea voluptate velit esse quam nihil molestiae consequatur, vel illum qui dolorem eum fugiat quo voluptas nulla pariatur</p></div>
  <div class="abs intro-col" style="left:463px"><h3>Lorem ipsum</h3><p>Quis autem vel eum iure reprehenderit qui in ea voluptate velit esse quam nihil molestiae consequatur, vel illum qui dolorem eum fugiat quo voluptas nulla pariatur</p></div>
  <div class="abs intro-col" style="left:807px"><h3>Lorem ipsum</h3><p>Quis autem vel eum iure reprehenderit qui in ea voluptate velit esse quam nihil molestiae consequatur, vel illum qui dolorem eum fugiat quo voluptas nulla pariatur</p></div>
  <a class="abs btn btn-facts">Nutritional Facts</a>
</section>

<section>
  <div class="abs about-script" aria-hidden="true">Mira Nutrition</div>
  <h2 class="abs about-title">About Me</h2>
  <p class="abs about-text">I am a clinical nutritionist with a Bachelors of Science and Masters of Science in Nutrition. I have over 30 years experience working with both inpatient and outpatient populations covering a myriad of conditions requiring nutritional intervention. I am passionate about my field and my goal is to help others achieve their optimal nutritional health.</p>
</section>

<section>
  <div class="abs blog-band"></div>
  <h2 class="abs blog-title">Blog</h2>

  <article class="abs post-card" style="left:75px">
    <div class="post-tags"><span>INFORMATIONAL</span><span>FITNESS TIPS</span></div>
    <div class="post-cat">NUTRITION</div>
    <h4>Nor again is there anyone who loves or pursues or desires to obtain</h4>
    <p>Quis autem vel eum iure reprehenderit qui in ea voluptate velit esse quam nihil molestiae consequatur, vel illum qui dolorem eum fugiat quo voluptas nulla pariatur</p>
    <div class="post-meta"><span class="date"><svg width="22" height="18" viewBox="0 0 22 18" fill="none" stroke="#aaa" stroke-width="1.2"><rect x="1" y="2" width="20" height="15"/><line x1="1" y1="6" x2="21" y2="6"/><line x1="6" y1="0" x2="6" y2="3"/><line x1="16" y1="0" x2="16" y2="3"/></svg>Feb 10, 2021</span><svg width="18" height="18" viewBox="0 0 18 18" fill="none" stroke="#aaa" stroke-width="1.2"><path d="M10 2H16V8"/><path d="M16 2L8 10"/><path d="M13 11V16H2V5H7"/></svg></div>
  </article>

  <article class="abs post-card" style="left:436px">
    <div class="post-tags"><span>INFORMATIONAL</span><span>FITNESS TIPS</span></div>
    <div class="post-cat">NUTRITION</div>
    <h4>Nor again is there anyone who loves or pursues or desires to obtain</h4>
    <p>Quis autem vel eum iure reprehenderit qui in ea voluptate velit esse quam nihil molestiae consequatur, vel illum qui dolorem eum fugiat quo voluptas nulla pariatur</p>
    <div class="post-meta"><span class="date"><svg width="22" height="18" viewBox="0 0 22 18" fill="none" stroke="#aaa" stroke-width="1.2"><rect x="1" y="2" width="20" height="15"/><line x1="1" y1="6" x2="21" y2="6"/><line x1="6" y1="0" x2="6" y2="3"/><line x1="16" y1="0" x2="16" y2="3"/></svg>Feb 10, 2021</span><svg width="18" height="18" viewBox="0 0 18 18" fill="none" stroke="#aaa" stroke-width="1.2"><path d="M10 2H16V8"/><path d="M16 2L8 10"/><path d="M13 11V16H2V5H7"/></svg></div>
  </article>

  <article class="abs post-card" style="left:797px">
    <div class="post-tags"><span>INFORMATIONAL</span><span>FITNESS TIPS</span></div>
    <div class="post-cat">NUTRITION</div>
    <h4>Nor again is there anyone who loves or pursues or desires to obtain</h4>
    <p>Quis autem vel eum iure reprehenderit qui in ea voluptate velit esse quam nihil molestiae consequatur, vel illum qui dolorem eum fugiat quo voluptas nulla pariatur</p>
    <div class="post-meta"><span class="date"><svg width="22" height="18" viewBox="0 0 22 18" fill="none" stroke="#aaa" stroke-width="1.2"><rect x="1" y="2" width="20" height="15"/><line x1="1" y1="6" x2="21" y2="6"/><line x1="6" y1="0" x2="6" y2="3"/><line x1="16" y1="0" x2="16" y2="3"/></svg>Feb 10, 2021</span><svg width="18" height="18" viewBox="0 0 18 18" fill="none" stroke="#aaa" stroke-width="1.2"><path d="M10 2H16V8"/><path d="M16 2L8 10"/><path d="M13 11V16H2V5H7"/></svg></div>
  </article>

  <a class="abs btn btn-more">View More Blog</a>
</section>

<section>
  <h2 class="abs archive-title">Archive</h2>

  <article class="abs archive-card" style="left:74px;top:1925px;width:511px;height:457px">
    <h4>Nor again is there anyone who loves or pursues or desires to obtain</h4>
    <p style="margin-top:24px">But I must explain to you how all this mistaken idea of denouncing pleasure and praising pain was born and</p>
    <p>I will give you a complete account of the system, and expound the actual teachings of the great explorer of the truth, the master-builder of human happiness.Nor again is there anyone who loves or pursues or desires to obtain pain of...</p>
    <p>Lorem ipsum dolor sit amet, consectetur adipiscing elit, sed do eiusmod tempor incididunt ut labore et dolore magna aliqua. Ut enim ad minim veniam, quis nostrud exercitation ullamco laboris nisi ut aliquip ex ea commodo consequat.</p>
    <div class="archive-date"><svg width="22" height="18" viewBox="0 0 22 18" fill="none" stroke="#fff" stroke-width="1.2"><rect x="1" y="2" width="20" height="15"/><line x1="1" y1="6" x2="21" y2="6"/><line x1="6" y1="0" x2="6" y2="3"/><line x1="16" y1="0" x2="16" y2="3"/></svg>Jan 10, 2020</div>
  </article>

  <article class="abs archive-card" style="left:612px;top:1927px;width:510px;height:213px">
    <h4>Nor again is there anyone who loves or pursues or desires to obtain</h4>
    <p style="margin-top:14px">Quis autem vel eum iure reprehenderit qui in ea voluptate velit esse quam nihil molestiae consequatur, vel illum qui dolorem eum fugiat quo voluptas nulla pariatur</p>
    <div class="archive-date" style="margin-top:12px"><svg width="22" height="18" viewBox="0 0 22 18" fill="none" stroke="#fff" stroke-width="1.2"><rect x="1" y="2" width="20" height="15"/><line x1="1" y1="6" x2="21" y2="6"/><line x1="6" y1="0" x2="6" y2="3"/><line x1="16" y1="0" x2="16" y2="3"/></svg>Jan 10, 2020</div>
  </article>

  <article class="abs archive-card" style="left:612px;top:2168px;width:510px;height:213px">
    <h4>Nor again is there anyone who loves or pursues or desires to obtain</h4>
    <p style="margin-top:14px">Quis autem vel eum iure reprehenderit qui in ea voluptate velit esse quam nihil molestiae consequatur, vel illum qui dolorem eum fugiat quo voluptas nulla pariatur</p>
    <div class="archive-date" style="margin-top:12px"><svg width="22" height="18" viewBox="0 0 22 18" fill="none" stroke="#fff" stroke-width="1.2"><rect x="1" y="2" width="20" height="15"/><line x1="1" y1="6" x2="21" y2="6"/><line x1="6" y1="0" x2="6" y2="3"/><line x1="16" y1="0" x2="16" y2="3"/></svg>Jan 10, 2020</div>
  </article>
</section>

<section class="abs partner-band">
  <span class="partner">Northtrail</span>
  <span class="partner">Stridewell</span>
  <span class="partner">Flowmotion</span>
  <span class="partner">Corepath</span>
  <span class="partner">Vantra</span>
</section>

<footer>
  <h3 class="abs foot-h" style="left:92px;top:2658px">Contact Us</h3>
  <div class="abs contact-row" style="top:2730px">
    <svg width="18" height="22" viewBox="0 0 18 22"><path d="M9 0C4 0 0 4 0 8.5 0 14 9 22 9 22S18 14 18 8.5C18 4 14 0 9 0Z" fill="var(--gold)"/><circle cx="9" cy="8.5" r="3.2" fill="#fff"/></svg>
    <span>Dolore magnam aliquam<br>quaerat voluptatem.</span>
  </div>
  <div class="abs contact-row" style="top:2796px">
    <svg width="20" height="20" viewBox="0 0 20 20"><path d="M4 1L8 5 6 8C7 11 9 13 12 14L15 12 19 16 16 19C8 18 2 12 1 4Z" fill="var(--gold)"/></svg>
    <span>0800 410 22 37<br>0900 733 18 60</span>
  </div>
  <div class="abs contact-row" style="top:2863px">
    <svg width="20" height="16" viewBox="0 0 20 16"><rect width="20" height="16" rx="1" fill="var(--gold)"/><path d="M1 2L10 9 19 2" stroke="#fff" stroke-width="1.5" fill="none"/></svg>
    <span>Theplateledger@mailnest.example</span>
  </div>

  <h3 class="abs foot-h" style="left:508px;top:2658px">Menu</h3>
  <div class="abs menu-row" style="top:2730px"><svg width="8" height="12" viewBox="0 0 8 12"><path d="M1 1L6 6 1 11" stroke="var(--gold)" stroke-width="1.6" fill="none"/></svg><span>Home</span></div>
  <div class="abs menu-row" style="top:2764px"><svg width="8" height="12" viewBox="0 0 8 12"><path d="M1 1L6 6 1 11" stroke="var(--gold)" stroke-width="1.6" fill="none"/></svg><span>About Me</span></div>
  <div class="abs menu-row" style="top:2797px"><svg width="8" height="12" viewBox="0 0 8 12"><path d="M1 1L6 6 1 11" stroke="var(--gold)" stroke-width="1.6" fill="none"/></svg><span>Services</span></div>
  <div class="abs menu-row" style="top:2830px"><svg width="8" height="12" viewBox="0 0 8 12"><path d="M1 1L6 6 1 11" stroke="var(--gold)" stroke-width="1.6" fill="none"/></svg><span>Blog</span></div>
  <div class="abs menu-row" style="top:2863px"><svg width="8" height="12" viewBox="0 0 8 12"><path d="M1 1L6 6 1 11" stroke="var(--gold)" stroke-width="1.6" fill="none"/></svg><span>Contact Us</span></div>

  <div class="abs foot-brand">
    <span class="brand-dot"></span>
    <span class="brand-name">The Plate<br>Ledger</span>
  </div>
  <span class="abs social" style="left:845px" aria-label="Social profile one"></span>
  <span class="abs social" style="left:893px" aria-label="Social profile two"></span>
  <span class="abs social" style="left:943px" aria-label="Social profile three"></span>

  <p class="abs copyright">© 2021 &nbsp;&nbsp;|&nbsp;&nbsp; www.plateledger.example</p>
</footer>

</body>
</html>
```